Welding and farication business card

Business name Tbm Welding & Fabrication

I need a business card made for my welding and fabrication business that is bold and stands out. My business is both welding repairs on machinery and anything else you can imagine as well as fabricating new products. i have used this service before and was very happy with the out come of my design logo. i think the card should remain fairly simple and classy but also be bold. I think a black card would best be suited to the talk with my logo on it. i feel the back of the card should just have my logo and the front have my logo email, website and phone number and maybe incorporate a facebook and instagram simple if it can be made look good these arnt a necessity.
I have included both my logo and some business card ideas below

Target Market(s)

Farmers, heavy industry, earthmoving, trucking

Industry/Entity Type

Engineering

Contact Information for Business Card

0438517264
dale@tbmweldingandfabrication.com.au
www.tbmweldingandfabrication.com.au

Colors
33a6d7
0255a3

Requirements
Must have
• Dale Hutchins
my phone number 0438517264
my logo
Preferably a black card desgn
Nice to have
• List of what i do,
Sheds and carports
Ute trays
Stockyards
Trailers
Farm equipment
Stockcrates
Gateways and Entrances
Breakdowns
Maintenance
And lots more!

```html
<!DOCTYPE html>
<html lang="en">
<head>
<meta charset="utf-8">
<title>Tbm Welding &amp; Fabrication – Business Card</title>
<link rel="stylesheet" href="https://fonts.googleapis.com/css2?family=Montserrat:wght@600;700&family=Arimo:wght@400&display=swap">
<style>
  :root {
    --backdrop: #e4e4e4;
    --card: #2b2b2d;
    --card-edge: #0a3f86;
    --brand-blue: #0255a3;
    --accent-cyan: #33a6d7;
    --text-light: #e8e8e8;
    --text-muted: #cfcfcf;
    --rule: #9a9a9a;
  }
  * { margin: 0; padding: 0; box-sizing: border-box; }
  html, body {
    width: 1200px; height: 801px; overflow: hidden;
    background: var(--backdrop);
  }
  .stage {
    width: 1200px; height: 801px;
    display: flex; align-items: center; justify-content: center; gap: 40px;
  }
  .card {
    position: relative;
    width: 540px; height: 309px;
    background: var(--card);
    border-bottom: 4px solid var(--card-edge);
    box-shadow: 0 10px 24px rgba(0,0,0,0.25);
    overflow: hidden;
  }
  .brand {
    display: flex; align-items: center; gap: 12px;
    font-family: "Montserrat", sans-serif;
    font-weight: 700;
    color: var(--text-light);
    text-transform: uppercase;
    letter-spacing: 0.5px;
  }
  .brand-dot {
    width: 18px; height: 18px; border-radius: 50%;
    background: var(--brand-blue);
    flex: none;
  }
  /* Contact side */
  .card--contact .brand {
    position: absolute; top: 58px; right: 36px;
    font-size: 19px;
  }
  .card--contact .rule {
    position: absolute; top: 150px; left: 36px; right: 36px;
    height: 1px; background: var(--rule);
  }
  .holder-name {
    position: absolute; top: 170px; left: 36px;
    font-family: "Montserrat", sans-serif; font-weight: 600;
    font-size: 20px; color: var(--accent-cyan);
    text-transform: uppercase; letter-spacing: 0.5px;
  }
  .contact-list {
    position: absolute; top: 206px; left: 36px;
    list-style: none;
    font-family: "Arimo", sans-serif; font-size: 13px;
    color: var(--text-muted);
  }
  .contact-list li {
    display: flex; align-items: center; gap: 10px;
    height: 24px;
  }
  .contact-list svg { width: 14px; height: 14px; flex: none; }
  /* Services side */
  .card--services .brand {
    position: absolute; top: 78px; left: 0; right: 0;
    justify-content: center;
    font-size: 22px;
  }
  .service-list {
    position: absolute; top: 160px; left: 30px; right: 30px;
    font-family: "Arimo", sans-serif; font-size: 14px;
    color: var(--text-light);
    text-transform: uppercase; letter-spacing: 0.4px;
    text-align: center; line-height: 24px;
  }
  .service-list span { white-space: nowrap; }
  .bullet {
    display: inline-block; width: 7px; height: 7px; border-radius: 50%;
    background: var(--accent-cyan);
    margin: 0 6px 2px 8px; vertical-align: middle;
  }
</style>
</head>
<body>
<main class="stage">
  <section class="card card--contact" aria-label="Business card front">
    <div class="brand"><span class="brand-dot"></span>Tbm Welding &amp; Fabrication</div>
    <div class="rule"></div>
    <h1 class="holder-name">Dale Hutchins</h1>
    <ul class="contact-list">
      <li>
        <svg viewBox="0 0 16 16" aria-hidden="true"><path d="M4 1.5l2.2 3-1.4 1.6c.9 2 2.4 3.5 4.3 4.4l1.6-1.4 3 2.2-1.3 2.6C7.6 13.4 2.6 8.4 1.5 3z" fill="var(--accent-cyan)"/></svg>
        0438517264
      </li>
      <li>
        <svg viewBox="0 0 16 16" aria-hidden="true"><rect x="1.5" y="3.5" width="13" height="9" fill="none" stroke="var(--accent-cyan)" stroke-width="1.3"/><path d="M1.5 3.5l6.5 5 6.5-5" fill="none" stroke="var(--accent-cyan)" stroke-width="1.3"/></svg>
        dale@tbmweldingandfabrication.com.au
      </li>
      <li>
        <svg viewBox="0 0 16 16" aria-hidden="true"><g fill="none" stroke="var(--accent-cyan)" stroke-width="1.2"><circle cx="8" cy="8" r="6.5"/><ellipse cx="8" cy="8" rx="3" ry="6.5"/><path d="M1.5 8h13M2.5 4.7h11M2.5 11.3h11"/></g></svg>
        www.tbmweldingandfabrication.com.au
      </li>
    </ul>
  </section>

  <section class="card card--services" aria-label="Business card back">
    <div class="brand"><span class="brand-dot"></span>Tbm Welding &amp; Fabrication</div>
    <p class="service-list">
      <span><i class="bullet"></i>Sheds</span>
      <span><i class="bullet"></i>Ute Trays</span>
      <span><i class="bullet"></i>Cattle and Sheep Yards</span>
      <span><i class="bullet"></i>Trailers</span>
      <span><i class="bullet"></i>Farm Equipment</span>
      <span><i class="bullet"></i>Gateways and Entrances</span>
      <span><i class="bullet"></i>Breakdowns</span>
      <span><i class="bullet"></i>Maintenance</span>
      <span><i class="bullet"></i>And Lots More!</span>
    </p>
  </section>
</main>
</body>
</html>
```